Orlavin canola oil needs a lable design

We need to design a label for our ORLAVIN brand canola oil. We want our product to be easily noticed on supermarket shelves and clearly identified as Australian-made, distinguishing it from other canola oils. Our product is 100% Australian-made, non-GMO canola oil. The packaging size is 2 liters. The front and back label designs are required.
Updates

The label needs to be advanced, high-class and eye-catching. The Logo is just a reference and can be redesigned if there is a better idea.

I invited a new designer to create a design on Monday, but I haven't received the design work yet. I'm worried that my time might have expired and that he wasn't able to upload it.

Target Market(s)

high-end supermarket

Industry/Entity Type

cold pressed canola oil

Requirements
Must have
• 100% Australian-made,non-GMO,nutrition board,Kosher certification,Halal certification,HACCP
Nice to have
• easily be noticed at supermarket and clearly identified as Australian-made;different from the existing canola oil label design

```html
<!DOCTYPE html>
<html lang="en">
<head>
<meta charset="utf-8">
<title>Orlavin Canola Oil – Front Label</title>
<link rel="stylesheet" href="https://fonts.googleapis.com/css2?family=Abril+Fatface&family=Montserrat:wght@700;800&display=swap">
<style>
  :root {
    --backdrop: #ece2d4;
    --label-green: #0f7a4e;
    --label-green-deep: #0a5e3b;
    --line-green: #0d6843;
    --sun-yellow: #f6d21c;
    --petal-yellow: #f2b90f;
    --petal-core: #d99a06;
    --cream: #f6efe3;
    --ink-green: #0b3d27;
    --white: #ffffff;
  }
  * { box-sizing: border-box; margin: 0; padding: 0; }
  html, body {
    width: 1200px;
    height: 1200px;
    overflow: hidden;
    background: var(--backdrop);
  }
  .canvas {
    position: relative;
    width: 1200px;
    height: 1200px;
    display: flex;
    align-items: center;
    justify-content: center;
  }
  .label {
    position: relative;
    width: 542px;
    height: 1040px;
    border-radius: 12px;
    overflow: hidden;
    background: var(--label-green);
  }
  .label__botanical {
    position: absolute;
    inset: 0;
    background:
      radial-gradient(ellipse 40% 22% at 82% 14%, rgba(6, 70, 42, 0.55), transparent 70%),
      radial-gradient(ellipse 30% 18% at 88% 58%, rgba(6, 70, 42, 0.45), transparent 70%),
      radial-gradient(ellipse 18% 60% at 14% 45%, rgba(6, 70, 42, 0.5), transparent 70%),
      radial-gradient(ellipse 25% 20% at 10% 90%, rgba(6, 70, 42, 0.45), transparent 70%),
      linear-gradient(170deg, #118553 0%, var(--line-green) 60%, var(--label-green-deep) 100%);
  }
  .brand {
    position: absolute;
    top: 228px;
    left: 0;
    right: 0;
    display: flex;
    align-items: center;
    justify-content: center;
    gap: 14px;
  }
  .brand__dot {
    width: 22px;
    height: 22px;
    border-radius: 50%;
    background: var(--cream);
  }
  .brand__name {
    font-family: "Montserrat", sans-serif;
    font-weight: 700;
    font-size: 44px;
    letter-spacing: 6px;
    color: var(--cream);
  }
  .flower {
    position: absolute;
    top: 365px;
    left: 124px;
    width: 306px;
    height: 247px;
    border-radius: 46% 46% 50% 50%;
    background: radial-gradient(circle at 50% 42%, var(--petal-core) 0%, var(--petal-yellow) 30%, var(--sun-yellow) 75%, rgba(246, 210, 28, 0.9) 100%);
  }
  .product-name {
    position: absolute;
    top: 636px;
    left: 0;
    right: 0;
    text-align: center;
    font-family: "Abril Fatface", serif;
    font-weight: 400;
    color: var(--sun-yellow);
    text-shadow: 5px 5px 0 var(--ink-green);
    line-height: 0.94;
  }
  .product-name__line {
    display: block;
    font-size: 146px;
    transform: scaleX(0.6);
    transform-origin: center;
  }
  .badge-gmo {
    position: absolute;
    left: 79px;
    top: 895px;
    width: 96px;
    height: 96px;
    border-radius: 50%;
    background: var(--sun-yellow);
    display: flex;
    align-items: center;
    justify-content: center;
    text-align: center;
    font-family: "Montserrat", sans-serif;
    font-weight: 800;
    font-size: 22px;
    line-height: 1.02;
    color: var(--label-green);
  }
  .volume {
    position: absolute;
    left: 0;
    right: 0;
    top: 934px;
    text-align: center;
    font-family: "Montserrat", sans-serif;
    font-weight: 700;
    font-size: 29px;
    color: var(--white);
    letter-spacing: 1px;
  }
  .badge-origin {
    position: absolute;
    left: 369px;
    top: 864px;
    width: 130px;
    height: 114px;
  }
</style>
</head>
<body>
  <main class="canvas">
    <section class="label">
      <div class="label__botanical" role="img" aria-label="Engraved botanical line drawing of canola stems, buds, leaves and blossoms in deep green"></div>

      <div class="brand">
        <span class="brand__dot"></span>
        <span class="brand__name">ORLAVIN</span>
      </div>

      <div class="flower" role="img" aria-label="Photograph of a bright yellow four-petalled canola flower"></div>

      <h1 class="product-name">
        <span class="product-name__line">CANOLA</span>
        <span class="product-name__line">OIL</span>
      </h1>

      <p class="badge-gmo">NON<br>GMO</p>
      <p class="volume">2 LTR</p>
      <svg class="badge-origin" viewBox="0 0 130 114" role="img" aria-label="Origin certification badge">
        <polygon points="65,2 128,112 2,112" fill="var(--white)"/>
      </svg>
    </section>
  </main>
</body>
</html>
```